Brightfold (main name) sharpening systems(underneath)

Specializing in Knife, Scissors and Clipper sharpening, repair and maintenance.
I would like a logo designed that has at least one of the elements above showing what could happen as a result of the instrument being sharpened by my company as part of the logo (maybe the word Brightfold being cut in half)

Target Market(s)

commercial (restaurants or any establishment that deals with food preparation, salons, barbershops) residential (any homes that use knives scissors or clippers)

Contact Information for Business Card

Name: Dale Hovington
Address: C215 Corvell Heights Christ Church
Cell: 15559271836
Email: brightfoldsharp@mailtrovex.com

Requirements
Must have
• Brightfold....sharpening systems clean front with strong logo indicating what we do as part of logo front of card
• Contact details: back of card
• we sharpen on site or pick up and drop off within 24hrs (at back of Card)
• telephone number: (at back) for contact
• address and other details (at back)

```html
<!DOCTYPE html>
<html lang="en">
<head>
<meta charset="utf-8">
<title>Brightfold Sharpening Systems – Business Card</title>
<link rel="stylesheet" href="https://fonts.googleapis.com/css2?family=Cinzel:wght@500&family=Open+Sans:wght@400;700&display=swap">
<style>
  :root {
    --backdrop: #e7e4df;
    --front-center: #7a7a7a;
    --front-mid: #3c3c3c;
    --front-edge: #262626;
    --front-text: #e4e4e4;
    --logo-text: #d6d6d6;
    --back-top: #7e7e7e;
    --back-bottom: #f1f1f1;
    --back-band: #a6a6a6;
    --ink: #1b1b1b;
    --card-shadow: 0 4px 10px rgba(0,0,0,0.25);
  }
  html, body {
    margin: 0;
    padding: 0;
    width: 1200px;
    height: 1000px;
    overflow: hidden;
    background: var(--backdrop);
  }
  .canvas {
    position: relative;
    width: 1200px;
    height: 1000px;
  }
  .card {
    position: absolute;
    left: 266px;
    width: 666px;
    height: 397px;
    box-shadow: var(--card-shadow);
    overflow: hidden;
    font-family: "Open Sans", sans-serif;
  }
  /* Front */
  .card--front {
    top: 74px;
    background: radial-gradient(ellipse 55% 60% at 50% 45%, var(--front-center) 0%, var(--front-mid) 60%, var(--front-edge) 100%);
  }
  .brand {
    position: absolute;
    top: 140px;
    left: 0;
    right: 0;
    text-align: center;
    margin: 0;
    font-family: "Open Sans", sans-serif;
    font-weight: 700;
    font-size: 70px;
    letter-spacing: 1px;
    text-transform: uppercase;
    color: var(--logo-text);
    line-height: 1;
  }
  .tagline-front {
    position: absolute;
    top: 298px;
    left: 0;
    right: 0;
    text-align: center;
    margin: 0;
    font-size: 22px;
    color: var(--front-text);
  }
  /* Back */
  .card--back {
    top: 533px;
    background: linear-gradient(to bottom, var(--back-top) 0%, var(--back-bottom) 88%);
    color: var(--ink);
    text-align: center;
  }
  .card--back .band {
    position: absolute;
    left: 0;
    right: 0;
    bottom: 0;
    height: 32px;
    background: var(--back-band);
  }
  .holder {
    position: absolute;
    top: 80px;
    left: 0;
    right: 0;
    margin: 0;
    font-family: "Cinzel", serif;
    font-weight: 500;
    font-size: 29px;
    letter-spacing: 1px;
    text-transform: uppercase;
  }
  .icons {
    position: absolute;
    top: 160px;
    left: 0;
    right: 0;
    display: flex;
    justify-content: center;
    gap: 6px;
  }
  .icons svg { width: 14px; height: 14px; fill: var(--ink); }
  .contact {
    position: absolute;
    left: 0;
    right: 0;
    margin: 0;
    font-size: 16px;
    line-height: 1;
  }
  .contact--phone { top: 191px; }
  .contact--email { top: 215px; }
  .contact--address { top: 249px; }
  .divider {
    position: absolute;
    top: 292px;
    left: 318px;
    width: 30px;
    height: 2px;
    background: var(--ink);
  }
  .service-note {
    position: absolute;
    top: 318px;
    left: 0;
    right: 0;
    margin: 0;
    font-size: 16px;
    line-height: 1;
  }
</style>
</head>
<body>
<div class="canvas">
  <section class="card card--front">
    <h1 class="brand">Brightfold</h1>
    <p class="tagline-front">Sharpening Systems</p>
  </section>

  <section class="card card--back">
    <h2 class="holder">Dale Hovington</h2>
    <div class="icons" aria-hidden="true">
      <svg viewBox="0 0 16 16"><path d="M1 6c0-2 3-3 7-3s7 1 7 3v1h-4V5.5H5V7H1z"/><path d="M4 8h8l2 5H2z"/></svg>
      <svg viewBox="0 0 16 16"><path d="M1 3h14v10H1z" fill="none"/><path d="M1 3h14L8 9z"/><path d="M1 4.5l7 5.5 7-5.5V13H1z"/></svg>
      <svg viewBox="0 0 16 16"><path d="M8 1l7 6.5h-2V15H9.5v-4h-3v4H3V7.5H1z"/></svg>
    </div>
    <p class="contact contact--phone">15559271836</p>
    <p class="contact contact--email">brightfoldsharp@mailtrovex.com</p>
    <p class="contact contact--address">C215 Corvell Heights Christ Church</p>
    <div class="divider"></div>
    <p class="service-note">We sharpen on site or pick up and drop off within 24hrs</p>
    <div class="band"></div>
  </section>
</div>
</body>
</html>
```